Infografik für Tanzschule
Zielgruppe
Wir sind eine Tanzschule für die Tänze Salsa, Bachata, kizomba & Zouk in Freiburg
Aufgabenstellung
DESIGN-BRIEFING
Tarifübersicht – Tanzschule Ritmo del Alba
Projektziel
Gestaltung einer klaren, hochwertigen Tarifübersicht für eine Tanzschule.
Die Grafik dient: als Information & Orientierung auf der Homepage, als visuelle Grundlage für das Anmeldeformular vor Ort, Der Einstieg erfolgt immer über eine gratis Schnupperstunde.
Die verbindliche Anmeldung erfolgt nach der Schnupperstunde vor Ort über ein Formular mit Auswahlkästchen.
Grundaufbau
3 Tarifkarten nebeneinander
Einheitlicher, moderner Stil
evtl. Emotionale Bilder (echte Tanzszenen, echte Menschen)
Klare Hierarchie:
Titel → Preis → Erklärung → Vorteile → Auswahlkästchen
Struktur der Tarifkarten
KARTE 1 – EINSTIEG
Titel: 1× PRO WOCHE TANZEN
Preis: 56 €/ 39 € erm.
Subline: pro Person · pro Kalendermonat
Vorteile (max. 4 Bulletpoints):
Ein fester wöchentlicher Kurs
Klare Routine & Struktur
Ausweichstunde im selben Monat möglich (muss klar enthalten sein)
Auswahl: ☐ 1× pro Woche tanzen
KARTE 2 – REGELMÄSSIG TANZEN (darf visuell leicht hervorgehoben sein, z. B. Rahmen oder Badge)
Optionales Badge:
SEHR BELIEBT
Titel: 2× PRO WOCHE TANZEN
Preis: 98 € / 68 € erm.
Vorteile:
Zwei feste wöchentliche Kurse
Mehr Praxis & schnellerer Fortschritt
Ausweichstunde im selben Monat möglich
Auswahl:
☐ 2× pro Woche tanzen
KARTE 3 – MAXIMALE FREIHEIT
Titel: FLAT – ALL YOU CAN DANCE
Preis: ab 129 € / 99 € erm.
Alle Tänze
Alle Kurse (für dein Tanz-Level)
Alle Workshops (für dein Tanz-Level)
Maximale Freiheit
☐ FLAT 1 Monat – 149 € | 119 € erm. (monatlich kündbar)
☐ FLAT 3 Monate – 129 € | 99 € erm. (3 Monate Erstlaufzeit)
Einheitlicher Hinweis unter den Karten (kleiner Text)
Ausweic..

```html
<!DOCTYPE html>
<html lang="de">
<head>
<meta charset="utf-8">
<title>Unsere Tarife – Ritmo del Alba</title>
<link href="https://fonts.googleapis.com/css2?family=Poppins:wght@300;400;500&display=swap" rel="stylesheet">
<style>
  :root {
    --page: #ffffff;
    --crimson: #b21a50;
    --ink: #1d1d3a;
    --price-grey: #5d6e67;
    --band-grey: #e6e6e3;
    --band-rose: #f5e6e2;
    --card-grey-top: #f7f5f4;
    --card-grey-bottom: #e4e4e1;
    --card-rose-top: #fbf6f5;
    --card-rose-bottom: #f3dcd8;
    --button-line: #8a6bd6;
    --button-fill: #f3f1f4;
    --photo-a: #1f3a4a;
    --photo-b: #6b2e2c;
    --photo-c: #2c4f5e;
  }
  * { box-sizing: border-box; margin: 0; padding: 0; }
  html, body { width: 1200px; height: 800px; overflow: hidden; }
  body {
    background: var(--page);
    font-family: "Poppins", sans-serif;
    color: var(--ink);
    position: relative;
  }
  .page-title {
    position: absolute; left: 0; width: 1178px; top: 94px;
    text-align: center; font-weight: 400; font-size: 54px;
    color: var(--crimson); letter-spacing: 0.5px;
  }
  .page-intro {
    position: absolute; left: 0; width: 1130px; top: 171px;
    text-align: center; font-size: 16.5px; font-weight: 400;
  }
  .brand {
    position: absolute; left: 893px; top: 134px;
    display: flex; align-items: center; gap: 8px;
    font-size: 18px; font-weight: 400; color: var(--crimson);
  }
  .brand-dot { width: 12px; height: 12px; border-radius: 50%; background: var(--crimson); }

  .tariff { position: absolute; border-radius: 0 0 26px 26px; }
  .tariff--grey { background: linear-gradient(180deg, var(--card-grey-top), var(--card-grey-bottom)); }
  .tariff--rose { background: linear-gradient(180deg, var(--card-rose-top), var(--card-rose-bottom)); }
  .tariff-photo {
    height: 53px;
    background: linear-gradient(100deg, var(--photo-a) 0%, var(--photo-b) 40%, var(--photo-c) 75%, var(--photo-b) 100%);
  }
  .tariff-title {
    height: 33px; display: flex; align-items: center; justify-content: center;
    font-size: 15.5px; font-weight: 400; letter-spacing: 0.2px;
  }
  .tariff--grey .tariff-title { background: var(--band-grey); }
  .tariff--rose .tariff-title { background: var(--band-rose); }

  .price { position: relative; height: 74px; }
  .price-currency { position: absolute; font-size: 22px; color: var(--price-grey); font-weight: 300; }
  .price-value { position: absolute; font-size: 56px; font-weight: 400; color: var(--price-grey); line-height: 1; }
  .price-reduced { position: absolute; font-size: 11px; color: var(--ink); white-space: nowrap; }
  .price-note { position: absolute; font-size: 8.5px; color: var(--price-grey); white-space: nowrap; }
  .tariff--accent .price-currency,
  .tariff--accent .price-value,
  .tariff--accent .price-reduced,
  .tariff--accent .price-note { color: var(--crimson); }
  .price-from { position: absolute; font-size: 17px; color: var(--ink); }

  .benefits { list-style: none; padding-left: 24px; padding-right: 10px; }
  .benefits li { position: relative; padding-left: 21px; font-size: 13.5px; line-height: 16.5px; }
  .benefits li svg { position: absolute; left: 0; top: 3px; }

  .choice {
    position: absolute; border: 1.3px solid var(--button-line); border-radius: 24px;
    background: var(--button-fill);
  }
  .choice-row { display: flex; align-items: center; gap: 8px; font-size: 15px; line-height: 20px; }
  .choice-box { width: 17px; height: 17px; border: 2px solid var(--ink); flex: none; }
  .choice-detail { font-size: 7.5px; line-height: 10px; padding-left: 25px; white-space: nowrap; }

  .terms {
    position: absolute; left: 164px; top: 668px; font-size: 12.8px; line-height: 17.5px;
  }
</style>
</head>
<body>
  <h1 class="page-title">Unsere Tarife</h1>
  <p class="page-intro">Der Einstieg erfolgt immer über eine kostenlose Schnupperstunde.</p>
  <div class="brand"><span class="brand-dot"></span>Ritmo del Alba</div>

  <section class="tariff tariff--grey" style="left:159px; top:241px; width:257px; height:297px;">
    <div class="tariff-photo" role="img" aria-label="Foto eines tanzenden Paares"></div>
    <div class="tariff-title">1× PRO WOCHE TANZEN</div>
    <div class="price">
      <span class="price-currency" style="left:34px; top:8px;">€</span>
      <span class="price-value" style="left:56px; top:9px;">56</span>
      <span class="price-reduced" style="left:131px; top:40px;">(39 € erm.)</span>
      <span class="price-note" style="left:62px; top:62px;">pro Person · pro Kalendermonat</span>
    </div>
    <ul class="benefits" style="margin-top:19px;">
      <li style="margin-bottom:9px;"><svg width="14" height="11" viewBox="0 0 14 11"><path d="M1 6l4 4 8-9" fill="none" stroke="#1d1d3a" stroke-width="1.6"/></svg>Ein fester wöchentlicher Kurs</li>
      <li style="margin-bottom:10px;"><svg width="14" height="11" viewBox="0 0 14 11"><path d="M1 6l4 4 8-9" fill="none" stroke="#1d1d3a" stroke-width="1.6"/></svg>Klare Routine &amp; Struktur</li>
      <li><svg width="14" height="11" viewBox="0 0 14 11"><path d="M1 6l4 4 8-9" fill="none" stroke="#1d1d3a" stroke-width="1.6"/></svg>Ausweichstunde im selben<br>Monat möglich</li>
    </ul>
  </section>
  <div class="choice" style="left:184px; top:518px; width:206px; height:43px; display:flex; align-items:center; padding-left:12px;">
    <div class="choice-row"><span class="choice-box"></span>1× pro Woche tanzen</div>
  </div>

  <section class="tariff tariff--rose tariff--accent" style="left:467px; top:236px; width:258px; height:373px;">
    <div class="tariff-photo" role="img" aria-label="Foto eines tanzenden Paares"></div>
    <div class="tariff-title" style="height:37px;">2× PRO WOCHE TANZEN</div>
    <div class="price">
      <span class="price-currency" style="left:34px; top:3px;">€</span>
      <span class="price-value" style="left:57px; top:4px;">98</span>
      <span class="price-reduced" style="left:132px; top:34px;">(68 € erm.)</span>
      <span class="price-note" style="left:61px; top:56px;">pro Person · pro Kalendermonat</span>
    </div>
    <ul class="benefits" style="margin-top:18px;">
      <li style="margin-bottom:19px;"><svg width="14" height="11" viewBox="0 0 14 11"><path d="M1 6l4 4 8-9" fill="none" stroke="#1d1d3a" stroke-width="1.6"/></svg>Zwei feste wöchentliche Kurse</li>
      <li style="margin-bottom:11px;"><svg width="14" height="11" viewBox="0 0 14 11"><path d="M1 6l4 4 8-9" fill="none" stroke="#1d1d3a" stroke-width="1.6"/></svg>Mehr Praxis &amp; schnellerer<br>Fortschritt</li>
      <li><svg width="14" height="11" viewBox="0 0 14 11"><path d="M1 6l4 4 8-9" fill="none" stroke="#1d1d3a" stroke-width="1.6"/></svg>Ausweichstunde im selben<br>Monat möglich</li>
    </ul>
  </section>
  <div class="choice" style="left:494px; top:581px; width:206px; height:42px; display:flex; align-items:center; padding-left:10px;">
    <div class="choice-row"><span class="choice-box"></span>2× pro Woche tanzen</div>
  </div>

  <section class="tariff tariff--grey" style="left:777px; top:238px; width:258px; height:423px;">
    <div class="tariff-photo" role="img" aria-label="Foto eines tanzenden Paares"></div>
    <div class="tariff-title" style="height:35px;">FLAT – ALL YOU CAN DANCE</div>
    <div class="price">
      <span class="price-currency" style="left:31px; top:7px; color:var(--ink);">€</span>
      <span class="price-from" style="left:30px; top:27px;">ab</span>
      <span class="price-value" style="left:55px; top:9px;">129</span>
      <span class="price-reduced" style="left:143px; top:39px;">(99 € erm.)</span>
      <span class="price-note" style="left:60px; top:60px; color:var(--ink);">pro Person · pro Kalendermonat</span>
    </div>
    <ul class="benefits" style="margin-top:44px; padding-left:29px;">
      <li style="margin-bottom:19px;"><svg width="14" height="11" viewBox="0 0 14 11"><path d="M1 6l4 4 8-9" fill="none" stroke="#1d1d3a" stroke-width="1.6"/></svg>Alle Tänze</li>
      <li style="margin-bottom:10px;"><svg width="14" height="11" viewBox="0 0 14 11"><path d="M1 6l4 4 8-9" fill="none" stroke="#1d1d3a" stroke-width="1.6"/></svg>Alle Workshops<br>(für dein Tanz-Level)</li>
      <li><svg width="14" height="11" viewBox="0 0 14 11"><path d="M1 6l4 4 8-9" fill="none" stroke="#1d1d3a" stroke-width="1.6"/></svg>Maximale Freiheit</li>
    </ul>
  </section>
  <div class="choice" style="left:808px; top:631px; width:206px; padding:15px 0 10px 16px;">
    <div class="choice-row"><span class="choice-box"></span>FLAT 1 Monat</div>
    <div class="choice-detail">149 € | 119 € erm. (monatlich kündbar)</div>
    <div class="choice-row" style="margin-top:9px;"><span class="choice-box"></span>FLAT 3 Monate</div>
    <div class="choice-detail">129 € | 99 € erm. (3 Monate Erstlaufzeit)</div>
  </div>

  <p class="terms">
    Die Anmeldung verlängert sich automatisch um jeweils einen Monat<br>
    und ist mit 14 Tagen Frist zum Monatsende kündbar.<br>
    Ausnahme: FLAT 3 Monate – kündbar nach Ablauf der Erstlaufzeit.
  </p>
</body>
</html>
```